Messianic Prophetic Timeline

I would like to create a timeline that will fit on a horizontal 11 x 8 1/2 (8 1/2 x11) sheet of paper.
I have two images that will need to be merged.
There should be 7 time points. 1) 457BCE-26 AD, 2) 26 AD-30AD, 3) 30 AD-66 AD, 4) 66AD- 70AD 5) 70 AD, 6) 70AD-20??, and 7) Future
The #6 and #7 from each graphic should be merged. The 30AD-70AD can be dropped. Time point #7 Future has two different texts both need to be preserved, I would like time point #7 to be larger than the other time points.
There are scripture verses that are associated with each block that should be preserved and be more prominent.
These images are from a powerpoint slide, but I want something that can be printed out.
I run a website www.brightcoverstudy.org. I have some brand colors that if can be incorporated or at least have some color cohesion would be great, but that is not as important as readability.
Background images are nice - The idea is one of conflict between light and darkness, two opposing forces, Christ and anti-Christ. Maybe a king on a white horse battling a large serpent dragon
If you can incorporate this quote near timeblock #1-2 "From the decree to restore Jerusalem until Messiah 483 year"
Second quote anywhere "He will make a covenant with many for 7 years"

```html
<!DOCTYPE html>
<html lang="en">
<head>
<meta charset="utf-8">
<title>Messianic Prophetic Timeline</title>
<link rel="stylesheet" href="https://fonts.googleapis.com/css2?family=Gilda+Display&family=Quicksand:wght@500;600;700&display=swap">
<style>
  :root {
    --header-green: #0b4f4d;
    --teal: #00b4b4;
    --purple: #7a0098;
    --date-purple: #78109a;
    --ink: #2a2a2a;
    --rule: #333a40;
    --connector: #15242f;
    --card-white: #ffffff;
  }
  * { margin: 0; padding: 0; box-sizing: border-box; }
  html, body { width: 1200px; height: 927px; overflow: hidden; }
  body { font-family: "Quicksand", sans-serif; background: #ffffff; }

  .sheet { position: relative; width: 1200px; height: 927px; overflow: hidden; }

  .backdrop {
    position: absolute; inset: 81px 0 0 0;
    background:
      radial-gradient(ellipse 360px 260px at 680px 420px, rgba(120,125,190,0.55), transparent 70%),
      radial-gradient(ellipse 260px 200px at 1080px 360px, rgba(150,150,205,0.45), transparent 70%),
      radial-gradient(ellipse 200px 300px at 360px 720px, rgba(70,70,95,0.55), transparent 70%),
      linear-gradient(180deg, #b59bc6 0%, #d8a6b6 28%, #eab189 52%, #dc9563 72%, #a7735a 88%, #6d5a5e 100%);
  }

  .masthead {
    position: absolute; left: 0; top: 0; width: 1200px; height: 81px;
    background: var(--header-green);
    display: flex; align-items: center; justify-content: center;
  }
  .masthead h1 {
    font-family: "Gilda Display", serif; font-weight: 400;
    color: #ffffff; font-size: 50px; letter-spacing: 2px; line-height: 1;
    padding-top: 4px;
  }

  .connectors { position: absolute; left: 0; top: 0; width: 1200px; height: 927px; pointer-events: none; }

  .card {
    position: absolute; width: 222px; height: 354px;
    background: var(--card-white);
    border: 1px solid var(--teal);
    border-radius: 30px;
    overflow: hidden;
    text-align: center;
    color: var(--ink);
  }
  .card--future { border: 2px solid var(--purple); }

  .card__date {
    position: absolute; left: 0; right: 0; top: 46px;
    font-weight: 700; font-size: 26px; color: var(--date-purple); line-height: 1;
  }
  .card__band {
    position: absolute; left: 0; right: 0; top: 94px; height: 38px;
    background: var(--teal); color: #ffffff;
    font-weight: 700; font-size: 26px; line-height: 38px;
  }
  .card--future .card__band { background: var(--purple); }
  .card__phase {
    position: absolute; left: 0; right: 0; top: 148px;
    font-weight: 600; font-size: 23px; color: var(--date-purple); line-height: 1;
  }
  .card__rule {
    position: absolute; left: 34px; right: 34px; top: 190px; height: 1.5px;
    background: var(--rule);
  }
  .card__body {
    position: absolute; left: 8px; right: 8px; top: 203px;
    font-weight: 700; font-size: 17px; line-height: 22px;
  }
  .card--future .card__body { line-height: 27px; }
  .card__refs {
    position: absolute; left: 4px; right: 4px; top: 316px;
    font-weight: 600; font-size: 14.5px; line-height: 21px; color: #333333;
  }
  .card__refs--low { top: 307px; }

  .quote-panel {
    position: absolute; left: 36px; top: 547px; width: 279px; height: 364px;
    border-radius: 18px; overflow: hidden;
    border: 1px solid var(--purple);
  }
  .quote-panel__quotes {
    height: 230px; background: rgba(255,255,255,0.86);
    padding-top: 35px; text-align: center;
  }
  .quote {
    font-style: italic; font-weight: 500; font-size: 17px; line-height: 22px; color: #2b2b2b;
  }
  .quote + .quote { margin-top: 40px; }
  .quote-panel__brand {
    height: 134px; background: var(--purple); color: #ffffff;
    position: relative;
  }
  .brand-name {
    position: absolute; left: 42px; top: 34px;
    display: flex; align-items: center; gap: 10px;
    font-weight: 600; font-size: 22px; line-height: 1;
  }
  .brand-name__dot { width: 18px; height: 18px; border-radius: 50%; background: #ffffff; }
  .site-url {
    position: absolute; left: 0; right: 0; top: 100px; text-align: center;
    font-weight: 600; font-size: 20px; line-height: 1;
  }
</style>
</head>
<body>
<div class="sheet">
  <header class="masthead"><h1>MESSIANIC PROPHETIC TIMELINE</h1></header>

  <div class="backdrop" role="img" aria-label="Sunset sky scene of a knight battling a great winged serpent dragon"></div>

  <svg class="connectors" viewBox="0 0 2184 1688" preserveAspectRatio="none" aria-hidden="true">
    <path d="M142,548 V250 Q142,207 185,207 H570 Q612,207 612,250 V850 Q612,893 655,893 H1042 Q1085,893 1085,850 V250 Q1085,207 1128,207 H1514 Q1557,207 1557,250 V852 Q1557,895 1600,895 H1985 Q2027,895 2027,938 V1622 Q2027,1665 1984,1665 H1600 Q1557,1665 1557,1622 V1020 Q1557,977 1514,977 H1128 Q1085,977 1085,1020 V1612 Q1085,1655 1042,1655 H658 Q615,1655 615,1612 V1320"
      fill="none" stroke="#15242f" stroke-width="5"/>
    <circle cx="142" cy="562" r="14" fill="none" stroke="#15242f" stroke-width="5"/>
    <circle cx="615" cy="1305" r="14" fill="none" stroke="#15242f" stroke-width="5"/>
  </svg>

  <section class="card" style="left:93px; top:125px;">
    <div class="card__date">457 BCE - 26 AD</div>
    <div class="card__band">MESSIAH</div>
    <div class="card__phase">Cut Off</div>
    <div class="card__rule"></div>
    <div class="card__body">483 years from<br>decree</div>
    <div class="card__refs" style="top:318px;">Dan 9:26, Ezra 7,9:9</div>
  </section>

  <section class="card" style="left:354px; top:127px;">
    <div class="card__date">26 AD-30AD</div>
    <div class="card__band">COVENANT</div>
    <div class="card__phase">Made</div>
    <div class="card__rule"></div>
    <div class="card__body">Jesus Make<br>Covenant with Many,<br>stops Sacrifice</div>
    <div class="card__refs" style="top:318px;">Dan 9:27</div>
  </section>

  <section class="card" style="left:615px; top:127px;">
    <div class="card__date">30 AD-66 AD</div>
    <div class="card__band">APOSTLES</div>
    <div class="card__phase">Persecution</div>
    <div class="card__rule"></div>
    <div class="card__body">In Synagogue<br>By family,<br>friends By Kings</div>
    <div class="card__refs" style="top:318px;">Luke 21:12-19</div>
  </section>

  <section class="card" style="left:875px; top:127px;">
    <div class="card__date">66AD- 70AD</div>
    <div class="card__band">VENGEANCE</div>
    <div class="card__phase">Days of</div>
    <div class="card__rule"></div>
    <div class="card__body">Jerusalem<br>Surrounded<br>Flee</div>
    <div class="card__refs" style="top:316px;">Luke 21:20-23</div>
  </section>

  <aside class="quote-panel">
    <div class="quote-panel__quotes">
      <p class="quote">“From the decree to restore<br>Jerusalem until Messiah<br>483 year”</p>
      <p class="quote">“He will make a covenant<br>with many for 7 years”</p>
    </div>
    <div class="quote-panel__brand">
      <div class="brand-name"><span class="brand-name__dot"></span>Brightcover</div>
      <div class="site-url">www.brightcoverstudy.org</div>
    </div>
  </aside>

  <section class="card card--future" style="left:356px; top:548px;">
    <div class="card__date" style="top:48px;">FUTURE</div>
    <div class="card__band">COVENANT</div>
    <div class="card__phase">Made</div>
    <div class="card__rule"></div>
    <div class="card__body">Stops Sacrifice Causes<br>Abomination of<br>Desolation</div>
    <div class="card__refs card__refs--low">Luke 21:25+ Matt 24:15<br>Dan 9:27,11:31,12:11</div>
  </section>

  <section class="card" style="left:618px; top:548px;">
    <div class="card__date" style="top:48px;">70AD-20</div>
    <div class="card__band">GENTILES</div>
    <div class="card__phase">Time of</div>
    <div class="card__rule"></div>
    <div class="card__body">Trample<br>Jerusalem</div>
    <div class="card__refs card__refs--low" style="top:318px;">Lk 21:8-11,24 Mat 24:4-14</div>
  </section>

  <section class="card" style="left:874px; top:548px;">
    <div class="card__date" style="top:48px;">70 AD++</div>
    <div class="card__band">JERUSALEM</div>
    <div class="card__phase">Desolation</div>
    <div class="card__rule"></div>
    <div class="card__body">Dispersed in<br>nations</div>
    <div class="card__refs card__refs--low">Lk 21:24 Is 61:2 Hos 9:7<br>Dan 9:26</div>
  </section>
</div>
</body>
</html>
```